Larkhaven Meditation

Logo picture and I want it to say

yoga. meditation. sound healing

small sweet classes

Larkhaven-meditation.example

2417 West Orindale Ave Suite K
Alder Cove CA 90000

```html
<!DOCTYPE html>
<html lang="en">
<head>
<meta charset="utf-8">
<title>Larkhaven Meditation – Small Sweet Classes</title>
<link rel="stylesheet" href="https://fonts.googleapis.com/css2?family=Montserrat:wght@500;600;700&display=swap">
<style>
  :root {
    --ink: #262527;
    --lavender: #a48bc6;
    --white: #ffffff;
    --stage: #6e6e6e;
    --photo-light: #eceae6;
    --photo-mid: #b9b8b6;
    --photo-floor: #9fb4c4;
  }
  * { margin: 0; padding: 0; box-sizing: border-box; }
  html, body { width: 737px; height: 1200px; overflow: hidden; }
  body {
    background: var(--stage);
    font-family: "Montserrat", Arial, sans-serif;
    position: relative;
  }
  .flyer {
    position: absolute;
    left: 18px; top: 129px;
    width: 700px; height: 941px;
    overflow: hidden;
    background: var(--ink);
  }
  .studio-photo {
    position: absolute; inset: 0;
    background:
      linear-gradient(180deg, rgba(255,255,255,0) 55%, var(--photo-floor) 100%),
      linear-gradient(100deg, var(--photo-mid) 0%, var(--photo-light) 25%, #f7f6f3 55%, var(--photo-mid) 100%);
  }
  .shapes { position: absolute; inset: 0; }
  .brand-seal {
    position: absolute;
    left: 500px; top: 27px;
    width: 168px; height: 168px;
    border-radius: 50%;
    background: #f3f1ee;
    border: 11px solid var(--lavender);
    display: flex; align-items: center; justify-content: center;
    text-align: center;
  }
  .brand-name {
    font-weight: 600;
    font-size: 16px;
    line-height: 1.2;
    color: #4a4a4c;
  }
  .headline {
    position: absolute;
    left: 29px; top: 494px;
    border-left: 3px solid var(--lavender);
    padding-left: 13px;
    font-weight: 600;
    font-size: 48px;
    line-height: 43px;
    letter-spacing: 0.5px;
  }
  .headline span { display: block; color: var(--lavender); }
  .headline .accent { color: var(--white); }
  .services {
    position: absolute;
    left: 29px; top: 663px;
    width: 604px; height: 47px;
    background: var(--lavender);
    border-radius: 0 24px 24px 0;
    color: var(--white);
    font-weight: 700;
    font-size: 27px;
    line-height: 47px;
    padding-left: 16px;
    white-space: nowrap;
  }
  .details {
    position: absolute;
    left: 29px; top: 746px;
    color: var(--white);
    font-weight: 500;
    font-size: 18.5px;
    line-height: 22px;
  }
  .detail-row { display: flex; align-items: flex-start; gap: 10px; margin-bottom: 12px; }
  .detail-row svg { flex: none; margin-top: 3px; }
  .cta {
    position: absolute;
    left: 29px; top: 842px;
    color: var(--lavender);
    font-weight: 700;
    font-size: 20px;
    line-height: 24px;
  }
  .phone {
    position: absolute;
    left: 29px; top: 866px;
    color: var(--white);
    font-weight: 700;
    font-size: 41px;
    line-height: 48px;
  }
</style>
</head>
<body>
  <main class="flyer">
    <div class="studio-photo" role="img" aria-label="Photo of three people in a bright yoga studio with tall windows, holding a low lunge with arms raised, on blue mats"></div>

    <svg class="shapes" width="700" height="941" viewBox="0 0 700 941" aria-hidden="true">
      <path d="M468,0 H700 V222 C650,185 620,110 584,111 C560,60 520,20 468,0 Z" fill="var(--lavender)"/>
      <path d="M500,0 H700 V190 C655,160 630,95 584,111 C565,55 540,25 500,0 Z" fill="var(--ink)"/>
      <path d="M0,360 C190,370 320,500 410,650 C480,770 580,815 700,830 V941 H0 Z" fill="var(--lavender)"/>
      <path d="M0,386 C180,395 300,520 390,670 C460,790 570,845 700,862 V941 H0 Z" fill="var(--ink)"/>
    </svg>

    <div class="brand-seal">
      <span class="brand-name">Larkhaven<br>Meditation</span>
    </div>

    <h1 class="headline">
      <span>SMALL</span>
      <span class="accent">SWEET</span>
      <span>CLASSES</span>
    </h1>

    <p class="services">YOGA • MEDITATION • SOUND HEALING</p>

    <div class="details">
      <p class="detail-row">
        <svg width="13" height="16" viewBox="0 0 13 16"><path d="M6.5,0.5 C3.2,0.5 0.8,3 0.8,6 C0.8,10 6.5,15.5 6.5,15.5 C6.5,15.5 12.2,10 12.2,6 C12.2,3 9.8,0.5 6.5,0.5 Z M6.5,8.2 A2.2,2.2 0 1 1 6.5,3.8 A2.2,2.2 0 1 1 6.5,8.2 Z" fill="var(--lavender)"/></svg>
        <span>2417 WEST ORINDALE AVE SUITE K ALDER<br>COVE CA 90000</span>
      </p>
      <p class="detail-row">
        <svg width="14" height="14" viewBox="0 0 14 14" fill="none" stroke="var(--lavender)" stroke-width="1.6"><circle cx="7" cy="7" r="6"/><ellipse cx="7" cy="7" rx="2.6" ry="6"/><path d="M1,7 H13 M2,4 H12 M2,10 H12"/></svg>
        <span>WWW.LARKHAVEN-MEDITATION.EXAMPLE</span>
      </p>
    </div>

    <p class="cta">FOR MORE DETAILS CONTACT US AT:</p>
    <p class="phone">(555) 014-2280</p>
  </main>
</body>
</html>
```